School District In Need of Powerful Presentation

Create a modern PPT design template -- standard and widescreen -- for the Brisco RE-8K school district inspired by its logo. The presentation should be a modern projection of 21st education that excites the people who view it. The school district is located in a rural farming community with a view of the rocky mountains to its west (check out this picture www.tentstopatmarlowbend.com/AnimatedImages/HomeGallery/000MountainScene.jpg). People in this community want quality education for their children with opportunities for them to be successful after they graduate.

Target Market(s)

The Johnstown and Milliken communities in Northern Colorado

Industry/Entity Type

Education

Font styles to use
Sans Serif

Colors
ec1f27
3176b5
acd036
fece3e
f78f20

Requirements
Must have
• The name of the school district:
• Brisco County School District RE-8K Ardenvale-Toller
• Website address: www.briscore8k.k12.zq.us/
• Email: listen@briscore8k.org
Nice to have
• A couple of color options including their current color scheme: red, gold, black
• Placeholder for pictures of students and teachers
Should not have
• Please do not use the full logo in it's current for, but you may use elements of the logo.

```html
<!DOCTYPE html>
<html lang="en">
<head>
<meta charset="utf-8">
<title>Brisco RE-8K Presentation Template</title>
<link href="https://fonts.googleapis.com/css2?family=Hind:wght@400;500;600;700&display=swap" rel="stylesheet">
<style>
  :root{
    --red:#ec1f27;
    --orange:#f78f20;
    --gold:#fece3e;
    --green:#acd036;
    --blue:#3176b5;
    --ink:#2b2b2b;
    --muted:#8a8a8a;
    --stage:#f2f2f2;
    --photo-a:#b98268;
    --photo-b:#5f4a44;
  }
  *{box-sizing:border-box;margin:0;padding:0}
  html,body{width:1200px;height:1200px;overflow:hidden}
  body{background:var(--stage);font-family:"Hind",sans-serif;color:var(--ink);position:relative}
  .stage-band{position:absolute;inset:0}
  .slide{position:absolute;background:#fff;overflow:hidden;box-shadow:0 1px 4px rgba(0,0,0,.16)}

  /* Cover */
  .cover{width:646px;height:363px;color:#fff;background:linear-gradient(180deg,var(--orange) 0%,#f46a22 55%,var(--red) 100%)}
  .cover--green{background:linear-gradient(180deg,#add236,#8fbf2e);color:#55661f}
  .cover--gold{background:linear-gradient(180deg,#fecf3e,#fbc233);color:#b07a12}
  .cover--blue{background:linear-gradient(180deg,#3579b8,#2d6fad);color:#fff}
  .cover__pill{position:absolute;left:54px;top:126px;height:22px;padding:0 10px;border:1px solid currentColor;border-radius:11px;font-size:8.6px;line-height:21px;white-space:nowrap;opacity:.95}
  .cover__title{position:absolute;left:54px;top:154px;font-size:32px;font-weight:700;letter-spacing:.3px;white-space:nowrap}
  .cover__subtitle{position:absolute;left:54px;top:197px;font-size:12.5px;font-weight:600}
  .cover__contact{position:absolute;left:54px;top:318px;font-size:8.4px;line-height:15px}
  .cover__contact b{font-weight:700}
  .thumb{transform-origin:0 0;transform:scale(.3855)}

  /* Content slides */
  .content{width:370px;height:207px}
  .kicker{position:absolute;left:0;right:0;top:19px;text-align:center;font-size:6px;font-weight:600;color:var(--red)}
  .heading{position:absolute;left:0;right:0;top:26px;text-align:center;font-size:10.5px;font-weight:700;color:var(--red);letter-spacing:.2px}
  .heading::after{content:"";display:block;width:28px;height:1px;background:var(--orange);margin:1px auto 0}
  .photo{position:absolute;background:linear-gradient(135deg,var(--photo-a),var(--photo-b))}
  .photo--warm{background:linear-gradient(160deg,#f06a3a,#e3322c 70%,#ec1f27)}
  .caption{position:absolute;left:40px;right:40px;top:149px;text-align:center;font-size:4.6px;line-height:6px;font-weight:500}
  .photo-label{position:absolute;bottom:5px;left:0;right:0;text-align:center;font-size:4.8px;color:#fff;font-weight:600}
  .footer{position:absolute;left:10px;right:10px;bottom:4px;border-top:1px solid #eee;padding-top:2px;font-size:3.2px;color:#bbb;display:flex;justify-content:space-between}

  .about-band{position:absolute;left:15px;width:340px;top:0;height:117px;background:linear-gradient(180deg,#f05a2e,#f07a30)}
  .about-band--blue{background:linear-gradient(180deg,#3a7cbb,#3176b5)}
  .about-band__org{position:absolute;left:0;right:0;top:44px;text-align:center;color:#fff;font-size:7.5px;font-weight:600}
  .about-band__title{position:absolute;left:0;right:0;top:54px;text-align:center;color:#fff;font-size:14px;font-weight:500}
  .feature{position:absolute;top:93px;width:62px;margin-left:-31px;text-align:center}
  .feature__icon{width:45px;height:45px;margin:0 auto;border-radius:50%;background:#fff;box-shadow:0 1px 3px rgba(0,0,0,.12);display:flex;align-items:center;justify-content:center;color:var(--orange)}
  .feature--blue .feature__icon{color:var(--blue)}
  .feature__icon svg{width:20px;height:20px}
  .feature__label{margin-top:9px;font-size:6.3px;font-weight:700;color:var(--orange)}
  .feature--blue .feature__label{color:var(--blue)}
  .feature__text{margin-top:3px;font-size:4.2px;line-height:5.6px;color:#666}

  .staff-tab{position:absolute;left:141px;top:0;width:96px;height:54px;background:linear-gradient(180deg,var(--orange),#f15a26);color:#fff;text-align:center}
  .staff-tab small{display:block;font-size:4.8px;margin-top:28px}
  .staff-tab strong{display:block;font-size:12px;font-weight:600;line-height:11px}
  .member{position:absolute;top:71px;width:70px;margin-left:-35px;text-align:center}
  .member__photo{width:52px;height:52px;border-radius:50%;background:#efefef;margin:0 auto}
  .member__name{margin-top:8px;font-size:6px;font-weight:700}
  .member__role{font-size:4.2px;font-weight:600}
  .member__text{margin-top:2px;font-size:4.2px;line-height:5.6px;color:#666}

  .feature-slide svg.layer{position:absolute;inset:0}
  .story{position:absolute;top:38px;width:150px;color:#fff}
  .story h2{font-size:14.5px;font-weight:700;letter-spacing:.2px;margin-bottom:3px}
  .story p{font-size:4.7px;line-height:5.5px;margin-bottom:5px}

  .main-point{position:absolute;left:0;right:0;top:100px;text-align:center;color:#fff;font-size:13px;font-weight:700;letter-spacing:.3px}
</style>
</head>
<body>

<svg class="stage-band" width="1200" height="1200" aria-hidden="true">
  <polygon points="0,560 1200,-20 1200,360 0,900" fill="#f8f8f8"/>
</svg>

<svg width="0" height="0" style="position:absolute" aria-hidden="true">
  <defs>
    <symbol id="i-clock" viewBox="0 0 24 24"><g fill="none" stroke="currentColor" stroke-width="1.2"><circle cx="12" cy="12" r="9"/><path d="M12 6v6l4 2"/></g></symbol>
    <symbol id="i-notebook" viewBox="0 0 24 24"><g fill="none" stroke="currentColor" stroke-width="1.2"><rect x="6" y="3" width="12" height="18" rx="1"/><path d="M9 3v18M4 7h4M4 12h4M4 17h4"/></g></symbol>
    <symbol id="i-star" viewBox="0 0 24 24"><path d="M12 3l2.7 5.6 6.1.8-4.5 4.2 1.1 6.1L12 16.8 6.6 19.7l1.1-6.1L3.2 9.4l6.1-.8z" fill="none" stroke="currentColor" stroke-width="1.2" stroke-linejoin="round"/></symbol>
    <symbol id="i-gift" viewBox="0 0 24 24"><g fill="none" stroke="currentColor" stroke-width="1.2"><rect x="4" y="9" width="16" height="11"/><rect x="3" y="6" width="18" height="3"/><path d="M12 6v14M12 6c-2-3-5-3-5-1s3 1 5 1c2 0 5 1 5-1s-3-2-5 1"/></g></symbol>
    <symbol id="i-pin" viewBox="0 0 24 24"><g fill="none" stroke="currentColor" stroke-width="1.2"><path d="M12 21s-6-6.5-6-11a6 6 0 0112 0c0 4.5-6 11-6 11z"/><circle cx="12" cy="10" r="2.2"/></g></symbol>
  </defs>
</svg>

<!-- Main cover -->
<section class="slide cover" style="left:22px;top:50px">
  <div class="cover__pill">Brisco County School District RE-8K Ardenvale-Toller</div>
  <h1 class="cover__title">PRESENTATION TITLE HERE</h1>
  <p class="cover__subtitle">Subtitle here</p>
  <p class="cover__contact"><b>Email.</b> listen@briscore8k.org<br><b>Website.</b> www.briscore8k.k12.zq.us</p>
</section>

<!-- Colour options -->
<div class="slide" style="left:679px;top:90px;width:249px;height:140px;box-shadow:none">
  <section class="slide cover thumb" style="left:0;top:0;box-shadow:none">
    <div class="cover__pill">Brisco County School District RE-8K Ardenvale-Toller</div>
    <h1 class="cover__title">PRESENTATION TITLE HERE</h1>
    <p class="cover__subtitle">Subtitle here</p>
    <p class="cover__contact"><b>Email.</b> listen@briscore8k.org<br><b>Website.</b> www.briscore8k.k12.zq.us</p>
  </section>
</div>
<div class="slide" style="left:940px;top:90px;width:247px;height:140px;box-shadow:none">
  <section class="slide cover cover--green thumb" style="left:0;top:0;box-shadow:none">
    <div class="cover__pill">Brisco County School District RE-8K Ardenvale-Toller</div>
    <h1 class="cover__title">PRESENTATION TITLE HERE</h1>
    <p class="cover__subtitle">Subtitle here</p>
    <p class="cover__contact"><b>Email.</b> listen@briscore8k.org<br><b>Website.</b> www.briscore8k.k12.zq.us</p>
  </section>
</div>
<div class="slide" style="left:679px;top:239px;width:249px;height:140px;box-shadow:none">
  <section class="slide cover cover--gold thumb" style="left:0;top:0;box-shadow:none">
    <div class="cover__pill">Brisco County School District RE-8K Ardenvale-Toller</div>
    <h1 class="cover__title">PRESENTATION TITLE HERE</h1>
    <p class="cover__subtitle">Subtitle here</p>
    <p class="cover__contact"><b>Email.</b> listen@briscore8k.org<br><b>Website.</b> www.briscore8k.k12.zq.us</p>
  </section>
</div>
<div class="slide" style="left:940px;top:239px;width:247px;height:140px;box-shadow:none">
  <section class="slide cover cover--blue thumb" style="left:0;top:0;box-shadow:none">
    <div class="cover__pill">Brisco County School District RE-8K Ardenvale-Toller</div>
    <h1 class="cover__title">PRESENTATION TITLE HERE</h1>
    <p class="cover__subtitle">Subtitle here</p>
    <p class="cover__contact"><b>Email.</b> listen@briscore8k.org<br><b>Website.</b> www.briscore8k.k12.zq.us</p>
  </section>
</div>

<!-- Row 1 -->
<section class="slide content" style="left:22px;top:459px">
  <p class="kicker">Main Content</p>
  <h2 class="heading">PRESENTATION TITLE HERE</h2>
  <div class="photo" style="left:0;top:57px;width:370px;height:84px;background:linear-gradient(180deg,#b9d3ea 0%,#d9d2c4 45%,#8a8173 75%,#6f8a4e 100%)" role="img" aria-label="Photo of a school building exterior"></div>
  <p class="caption">Lorem ipsum dolor sit amet, in eam wisi abhorreant omittantur, vulputate argumentum in eam. Nonumy senserit comprehensam vim ne, veritus maiorum repudiandae vix no. Cu usu feni reformidans, qui ius ipsum audire in.</p>
  <div class="footer"><span>Brisco County School District RE-8K Ardenvale-Toller</span><span>1</span></div>
</section>

<section class="slide content" style="left:416px;top:459px;width:368px">
  <p class="kicker">Main Content</p>
  <h2 class="heading">PRESENTATION TITLE HERE</h2>
  <div class="photo photo--warm" style="left:9px;top:60px;width:173px;height:115px" role="img" aria-label="Photo of students writing at a desk, red tint">
    <p class="photo-label">Lorem ipsum dolor sit amet.</p>
  </div>
  <div class="photo photo--warm" style="left:185px;top:60px;width:173px;height:115px" role="img" aria-label="Photo of a student working on paper, red tint">
    <p class="photo-label">Lorem ipsum dolor sit amet.</p>
  </div>
  <div class="footer"><span>Brisco County School District RE-8K Ardenvale-Toller</span><span>1</span></div>
</section>

<section class="slide content" style="left:809px;top:459px;width:369px">
  <div class="about-band" role="img" aria-label="Photo of students in class with orange overlay">
    <p class="about-band__org">BRISCO RE-8K</p>
    <p class="about-band__title">About us</p>
  </div>
  <div class="feature" style="left:62px"><div class="feature__icon"><svg><use href="#i-clock"/></svg></div><p class="feature__label">FEATURE #1</p><p class="feature__text">Audiam impedit periculis mea ea, essent intellegebat disputationi sed at.</p></div>
  <div class="feature" style="left:123px"><div class="feature__icon"><svg><use href="#i-notebook"/></svg></div><p class="feature__label">FEATURE #2</p><p class="feature__text">Audiam impedit periculis mea ea, essent intellegebat disputationi sed at.</p></div>
  <div class="feature" style="left:184px"><div class="feature__icon"><svg><use href="#i-star"/></svg></div><p class="feature__label">FEATURE #3</p><p class="feature__text">Audiam impedit periculis mea ea, essent intellegebat disputationi sed at.</p></div>
  <div class="feature" style="left:245px"><div class="feature__icon"><svg><use href="#i-gift"/></svg></div><p class="feature__label">FEATURE #4</p><p class="feature__text">Audiam impedit periculis mea ea, essent intellegebat disputationi sed at.</p></div>
  <div class="feature" style="left:306px"><div class="feature__icon"><svg><use href="#i-pin"/></svg></div><p class="feature__label">FEATURE #5</p><p class="feature__text">Audiam impedit periculis mea ea, essent intellegebat disputationi sed at.</p></div>
  <div class="footer"><span>Brisco County School District RE-8K Ardenvale-Toller</span><span>1</span></div>
</section>

<!-- Row 2 -->
<section class="slide content" style="left:22px;top:707px;height:206px">
  <div class="about-band about-band--blue" role="img" aria-label="Photo of students in class with blue overlay">
    <p class="about-band__org">BRISCO RE-8K</p>
    <p class="about-band__title">About us</p>
  </div>
  <div class="feature feature--blue" style="left:62px"><div class="feature__icon"><svg><use href="#i-clock"/></svg></div><p class="feature__label">FEATURE #1</p><p class="feature__text">Audiam impedit periculis mea ea, essent intellegebat disputationi sed at.</p></div>
  <div class="feature feature--blue" style="left:123px"><div class="feature__icon"><svg><use href="#i-notebook"/></svg></div><p class="feature__label">FEATURE #2</p><p class="feature__text">Audiam impedit periculis mea ea, essent intellegebat disputationi sed at.</p></div>
  <div class="feature feature--blue" style="left:184px"><div class="feature__icon"><svg><use href="#i-star"/></svg></div><p class="feature__label">FEATURE #3</p><p class="feature__text">Audiam impedit periculis mea ea, essent intellegebat disputationi sed at.</p></div>
  <div class="feature feature--blue" style="left:245px"><div class="feature__icon"><svg><use href="#i-gift"/></svg></div><p class="feature__label">FEATURE #4</p><p class="feature__text">Audiam impedit periculis mea ea, essent intellegebat disputationi sed at.</p></div>
  <div class="feature feature--blue" style="left:306px"><div class="feature__icon"><svg><use href="#i-pin"/></svg></div><p class="feature__label">FEATURE #5</p><p class="feature__text">Audiam impedit periculis mea ea, essent intellegebat disputationi sed at.</p></div>
  <div class="footer"><span>Brisco County School District RE-8K Ardenvale-Toller</span><span>1</span></div>
</section>

<section class="slide content" style="left:416px;top:707px;width:368px;height:206px">
  <div class="staff-tab"><small>About us</small><strong>Staff</strong></div>
  <div class="member" style="left:60px"><div class="member__photo" role="img" aria-label="Staff portrait placeholder"></div><p class="member__name">NAME HERE</p><p class="member__role">Job title</p><p class="member__text">Audiam impedit periculis mea ea, essent intellegebat disputationi sed at.</p></div>
  <div class="member" style="left:142px"><div class="member__photo" role="img" aria-label="Staff portrait placeholder"></div><p class="member__name">NAME HERE</p><p class="member__role">Job title</p><p class="member__text">Audiam impedit periculis mea ea, essent intellegebat disputationi sed at.</p></div>
  <div class="member" style="left:226px"><div class="member__photo" role="img" aria-label="Staff portrait placeholder"></div><p class="member__name">NAME HERE</p><p class="member__role">Job title</p><p class="member__text">Audiam impedit periculis mea ea, essent intellegebat disputationi sed at.</p></div>
  <div class="member" style="left:308px"><div class="member__photo" role="img" aria-label="Staff portrait placeholder"></div><p class="member__name">NAME HERE</p><p class="member__role">Job title</p><p class="member__text">Audiam impedit periculis mea ea, essent intellegebat disputationi sed at.</p></div>
  <div class="footer"><span>Brisco County School District RE-8K Ardenvale-Toller</span><span>1</span></div>
</section>

<section class="slide content feature-slide" style="left:809px;top:707px;width:369px;height:206px">
  <svg class="layer" viewBox="0 0 369 206" width="369" height="206">
    <defs><linearGradient id="g-orange-a" x1="0" y1="0" x2="0" y2="1"><stop offset="0" stop-color="#f78f20"/><stop offset="1" stop-color="#ec1f27"/></linearGradient></defs>
    <rect width="369" height="206" fill="url(#photo-tone)" role="img" aria-label="Photo of a student writing in class"/>
    <linearGradient id="photo-tone" x1="0" y1="0" x2="1" y2="1"><stop offset="0" stop-color="#9a7f70"/><stop offset=".6" stop-color="#5e5352"/><stop offset="1" stop-color="#3a3538"/></linearGradient>
    <circle cx="50" cy="104" r="160" fill="none" stroke="#fff" stroke-opacity=".55" stroke-width=".8"/>
    <circle cx="50" cy="104" r="152" fill="url(#g-orange-a)" opacity=".96"/>
  </svg>
  <div class="story" style="left:24px">
    <h2>TITLE HERE</h2>
    <p>Audiam impedit periculis mea ea, essent intellegebat disputationi sed at. Inciderint contentiones cum et, vix ut omnium detraxit concludaturque.</p>
    <p>Ne inermis albucius nam, an graeco fabulas vel. Quo eu sumo debet, te nec denique ponderum repudiandae.</p>
    <p>Qui ea deserunt rationibus constituto. Suscipit vituperata an vel, accusamus conclusionemque qui ei, nec ex alienum antiopam.</p>
  </div>
</section>

<!-- Row 3 -->
<section class="slide content feature-slide" style="left:22px;top:954px">
  <svg class="layer" viewBox="0 0 370 207" width="370" height="207">
    <defs>
      <linearGradient id="g-blue" x1="0" y1="0" x2="0" y2="1"><stop offset="0" stop-color="#3a7dbc"/><stop offset="1" stop-color="#2e6fab"/></linearGradient>
      <linearGradient id="photo-tone-b" x1="0" y1="0" x2="1" y2="1"><stop offset="0" stop-color="#9a7f70"/><stop offset=".6" stop-color="#5e5352"/><stop offset="1" stop-color="#3a3538"/></linearGradient>
    </defs>
    <rect width="370" height="207" fill="url(#photo-tone-b)" role="img" aria-label="Photo of a student writing in class"/>
    <circle cx="50" cy="104" r="160" fill="none" stroke="#fff" stroke-opacity=".55" stroke-width=".8"/>
    <circle cx="50" cy="104" r="152" fill="url(#g-blue)" opacity=".96"/>
  </svg>
  <div class="story" style="left:24px">
    <h2>TITLE HERE</h2>
    <p>Audiam impedit periculis mea ea, essent intellegebat disputationi sed at. Inciderint contentiones cum et, vix ut omnium detraxit concludaturque.</p>
    <p>Ne inermis albucius nam, an graeco fabulas vel. Quo eu sumo debet, te nec denique ponderum repudiandae.</p>
    <p>Qui ea deserunt rationibus constituto. Suscipit vituperata an vel, accusamus conclusionemque qui ei, nec ex alienum antiopam.</p>
  </div>
</section>

<section class="slide content feature-slide" style="left:416px;top:954px;width:368px">
  <svg class="layer" viewBox="0 0 368 207" width="368" height="207">
    <defs>
      <linearGradient id="g-orange-b" x1="0" y1="0" x2="0" y2="1"><stop offset="0" stop-color="#f78f20"/><stop offset="1" stop-color="#ec1f27"/></linearGradient>
      <linearGradient id="photo-tone-c" x1="0" y1="0" x2="1" y2="1"><stop offset="0" stop-color="#c0302c"/><stop offset=".5" stop-color="#9b7060"/><stop offset="1" stop-color="#6d5a52"/></linearGradient>
    </defs>
    <rect width="368" height="207" fill="url(#photo-tone-c)" role="img" aria-label="Photo of a young student writing with a pencil"/>
    <circle cx="320" cy="104" r="160" fill="none" stroke="#fff" stroke-opacity=".55" stroke-width=".8"/>
    <circle cx="320" cy="104" r="152" fill="url(#g-orange-b)" opacity=".96"/>
  </svg>
  <div class="story" style="left:210px">
    <h2>TITLE HERE</h2>
    <p>Audiam impedit periculis mea ea, essent intellegebat disputationi sed at. Inciderint contentiones cum et, vix ut omnium detraxit concludaturque.</p>
    <p>Ne inermis albucius nam, an graeco fabulas vel. Quo eu sumo debet, te nec denique ponderum repudiandae.</p>
    <p>Qui ea deserunt rationibus constituto. Suscipit vituperata an vel, accusamus conclusionemque qui ei, nec ex alienum antiopam.</p>
  </div>
</section>

<section class="slide content" style="left:809px;top:954px;width:369px;background:linear-gradient(180deg,#f5822a 0%,#f2612c 55%,#ec2f2a 100%)" role="img" aria-label="Photo of students in class with orange overlay">
  <p class="main-point">PLACE MAIN POINT HERE</p>
</section>

</body>
</html>
```